Classic and neutral book cover design

We are looking for a classic and neutral book cover design to be used as the template for a series of books to be published. We are hence looking for a template that will allow us to easily change the title name for all books in this series.
The use of very few colours (black and white is welcome) and few design elements is a big bonus. As a source of inspiration we would like to ask you to view the very simple and
If you think you have a cool idea that can add a twist to the formal classic look don't hesitate. Go for it !
Work will be done for a 30 year old Sweden based cultural non-profit called VĂ©lra (www.velrafoundation.example). We work with the publishing and supporting of post-modern art and literature addressing contemporary topics but are also involved in assisting projects of cultural preservation.
Target Market(s)
The audience is expected to have some form of interest in culture but could range from hobbyist readers to tenure track scholars
Industry/Entity Type
Non-Profit
Requirements
Must have
- General:
- Classic and neutral feel
- Preferably very simple and few shapes
- usage of few colours (black and white is welcome)
Information to be displayed on the cover is:
- Author
- Title
- type of work e.g. play/novel (optional)
- publishing house (in this case "Velra Publishing")
Nice to have
- ideas to prevent it from become boring are of course welcome
Should not have
- - too many colours

```html
<!DOCTYPE html>
<html lang="en">
<head>
<meta charset="utf-8">
<title>Book Cover – Velra Publishing</title>
<link rel="stylesheet" href="https://fonts.googleapis.com/css2?family=Poiret+One&family=Open+Sans:wght@600&display=swap">
<style>
  :root {
    --paper: #ffffff;
    --spine-teal: #5f8593;
    --band-dark: rgba(38, 38, 38, 0.92);
    --title-teal: #5f8593;
    --author-grey: #4a4a4a;
    --band-text: #ffffff;
  }
  * { margin: 0; padding: 0; box-sizing: border-box; }
  html, body {
    width: 851px;
    height: 1200px;
    overflow: hidden;
    background: var(--paper);
  }
  .cover {
    position: relative;
    width: 851px;
    height: 1200px;
    background: var(--paper);
    overflow: hidden;
  }
  .accent-stripe {
    position: absolute;
    left: 113px;
    top: 0;
    width: 75px;
    height: 1200px;
    background: var(--spine-teal);
    z-index: 1;
  }
  .band {
    position: absolute;
    left: 0;
    width: 851px;
    background: var(--band-dark);
    z-index: 2;
  }
  .band--top { top: 99px; height: 100px; }
  .band--bottom { top: 1061px; height: 57px; }
  .author {
    position: absolute;
    left: 192px;
    top: 228px;
    font-family: "Poiret One", sans-serif;
    font-size: 40px;
    line-height: 1;
    color: var(--author-grey);
    letter-spacing: 1px;
    z-index: 3;
  }
  .title {
    position: absolute;
    left: 190px;
    top: 256px;
    font-family: "Poiret One", sans-serif;
    font-size: 92px;
    line-height: 1;
    color: var(--title-teal);
    text-transform: uppercase;
    letter-spacing: 6px;
    font-weight: 400;
    white-space: nowrap;
    z-index: 3;
  }
  .publisher {
    position: absolute;
    right: 24px;
    top: 1061px;
    height: 57px;
    line-height: 57px;
    font-family: "Open Sans", sans-serif;
    font-weight: 600;
    font-size: 27px;
    color: var(--band-text);
    z-index: 3;
  }
</style>
</head>
<body>
  <main class="cover">
    <div class="accent-stripe"></div>
    <div class="band band--top"></div>
    <p class="author">author's</p>
    <h1 class="title">Book Title</h1>
    <div class="band band--bottom"></div>
    <p class="publisher">Velra Publishing</p>
  </main>
</body>
</html>
```